Townhome Multi-Family Property Exterior Sign

Hello. We are looking for a new design for our exterior pylon for for a multi-family housing property in Texas. The design will need to go on a new sign panel to replace the existing (see photo of existing). We are looking to see both modern and contemporary designs. Included the sign should be the name, Loma Brisa Townhomes and the web address www.lomabrisatownhomes.example.

Attached here is a PDF file of the proposed new sign shape. We are open to other shape ideas as well if your design would better suit a more rectangular shape.

Industry/Entity Type

Property

Font styles to use
Serif
Sans Serif

Colors
9bcb3c

Requirements
Must have
• Name of building: Loma Brisa Townhomes
• Website: www.lomabrisatownhomes.example
Nice to have
• Address: 412-590 Halvern Ridge Drive (only if it fits nicely)

```html
<!DOCTYPE html>
<html lang="en">
<head>
<meta charset="utf-8">
<title>Loma Brisa Townhomes — Exterior Sign</title>
<link rel="stylesheet" href="https://fonts.googleapis.com/css2?family=Alegreya+Sans:ital,wght@1,500;1,700&display=swap">
<style>
  :root {
    --backdrop: #e4e4e4;
    --panel: #333333;
    --panel-edge: #1f1f1f;
    --skyline: #444444;
    --band: #207548;
    --band-shadow: #1a5a37;
    --text-light: #ffffff;
    --title-shadow: rgba(0, 0, 0, 0.45);
  }
  html, body {
    margin: 0;
    padding: 0;
    overflow: hidden;
    background: var(--backdrop);
  }
  .sign-canvas {
    position: relative;
    width: 1200px;
    height: 729px;
    overflow: hidden;
    background: var(--backdrop);
    font-family: "Alegreya Sans", "Trebuchet MS", sans-serif;
    font-style: italic;
  }
  .sign-shape {
    position: absolute;
    inset: 0;
  }
  .skyline {
    position: absolute;
    left: 339px;
    top: 92px;
    width: 505px;
    height: 105px;
    background: linear-gradient(to bottom, rgba(68,68,68,0) 0%, var(--skyline) 40%, var(--skyline) 100%);
  }
  .name-band-shadow {
    position: absolute;
    left: 185px;
    top: 211px;
    width: 843px;
    height: 281px;
    background: var(--band-shadow);
  }
  .name-band {
    position: absolute;
    left: 171px;
    top: 197px;
    width: 843px;
    height: 281px;
    background: var(--band);
    display: flex;
    flex-direction: column;
    align-items: center;
    justify-content: center;
  }
  .property-name {
    margin: 0;
    color: var(--text-light);
    font-weight: 500;
    font-size: 112px;
    line-height: 112px;
    text-align: center;
    letter-spacing: 1px;
    text-shadow: 3px 3px 2px var(--title-shadow);
  }
  .property-name span { display: block; }
  .address {
    position: absolute;
    left: 264px;
    width: 670px;
    top: 520px;
    margin: 0;
    text-align: center;
    color: var(--text-light);
    font-weight: 500;
    font-size: 23px;
  }
  .website {
    position: absolute;
    left: 264px;
    width: 670px;
    top: 561px;
    margin: 0;
    text-align: center;
    color: var(--text-light);
    font-weight: 700;
    font-size: 32px;
  }
</style>
</head>
<body>
  <main class="sign-canvas">
    <svg class="sign-shape" width="1200" height="729" viewBox="0 0 1200 729" aria-hidden="true">
      <path d="M270 137 Q605 -61 940 137 L940 700 L270 700 Z" fill="var(--panel-edge)"/>
      <path d="M264 133 Q599 -65 934 133 L934 698 L264 698 Z" fill="var(--panel)"/>
    </svg>
    <div class="skyline" role="img" aria-label="City skyline silhouette in dark grey"></div>
    <div class="name-band-shadow"></div>
    <div class="name-band">
      <h1 class="property-name"><span>LOMA BRISA</span><span>TOWNHOMES</span></h1>
    </div>
    <p class="address">412-590 Halvern Ridge Drive</p>
    <p class="website">www.lomabrisatownhomes.example</p>
  </main>
</body>
</html>
```